Launching a new real estate agency in Monaco

Hello, I am opening a new real estate agency in Monaco. For the purpose of my activity, in order to be known quickly among a fierce competition I need an advertising campaign that will be broadcast in local magazines, newspapers, paper board, etc.

You will find example of pictures of Monaco on which I have the rights and my logo. You can always pick other images that I can buy if the price is reasonable for a commercial use (<200 $)

Please respect the color code.

I wish you good luck and look forward to give you my feedbacks

Reason: Only few projects posted were respecting the brief and of quality. Hoping to receive more in coming days

Target Market(s)

International high-end clientele of all ages, all genders.

Industry/Entity Type

Real Estate Agent

Font styles to use
Serif

Requirements
Must have
• 1/ My logo
• 2/ This message "Un nouveau regard sur l'immobilier" means in English a fresh look at real estate or new eyes on real-estate.
• 3/ My address: 14 rue des Orvilles, Passage Marcellin, 98 000 Monaco
• 4/ Phone number: +377.93.48.25.71
• 5/ Website: www.brunor-agency.com.
• 6/ Format: Files should be easily adjustable but I'd like a vertical display to fit easily in Magazines, Poster and billboard. So please work in high resolution !
Nice to have
• Please think about your design in accordance with the message I want to display.
Should not have
• A simple poster with a picture of Monaco that does not take into consideration the message of the advertisement, "Un nouveau regard sur l'immobilier" which means in english, new eyes on real-estate or a new look at real-estate, or new vision at real-estate.

```html
<!DOCTYPE html>
<html lang="fr">
<head>
<meta charset="utf-8">
<title>Brunor Agency – un nouveau regard sur l'immobilier</title>
<link rel="stylesheet" href="https://fonts.googleapis.com/css2?family=Arimo:wght@400;700&display=swap">
<style>
  :root {
    --backdrop: #cfd6d3;
    --frame: #1a1a1a;
    --navy: #1c2a45;
    --navy-deep: #16223a;
    --copper: #dc9a80;
    --copper-soft: #e7b6a1;
    --silver-light: #c9cacd;
    --silver-dark: #8e9096;
    --sea: #1f7fc2;
    --sky: #a9d3f0;
    --roof: #c0623f;
    --text-light: #e9e6e4;
  }
  * { box-sizing: border-box; margin: 0; padding: 0; }
  html, body {
    width: 960px; height: 1200px; overflow: hidden;
    background: var(--backdrop);
    font-family: "Arimo", Arial, sans-serif;
  }
  .poster {
    position: absolute; left: 180px; top: 35px;
    width: 600px; height: 1130px;
    background: linear-gradient(180deg, var(--navy) 0%, var(--navy-deep) 100%);
    border: 8px solid var(--frame);
    overflow: hidden;
  }
  .territory-map {
    position: absolute; left: 40px; top: 120px;
    width: 520px; height: 540px;
    background: radial-gradient(ellipse 50% 48% at 48% 50%,
      var(--silver-light) 0%, var(--silver-dark) 60%, rgba(142,144,150,0) 100%);
    opacity: 0.6;
  }
  .headline {
    position: absolute; right: 92px; top: 348px;
    text-align: right;
    font-weight: 700; font-size: 55px; line-height: 56px;
    letter-spacing: -1.5px;
    color: var(--copper);
  }
  .coast-photo {
    position: absolute; left: 0; top: 655px;
    width: 100%; height: 250px;
    background: linear-gradient(180deg, var(--sky) 0%, var(--sea) 38%, #2f6f8e 60%, var(--roof) 100%);
  }
  .brand {
    position: absolute; left: 0; right: 0; top: 925px;
    text-align: center;
  }
  .brand-name {
    display: inline-flex; align-items: center; gap: 14px;
    font-weight: 700; font-size: 38px; letter-spacing: 3px;
    color: var(--copper);
  }
  .brand-mark {
    width: 34px; height: 34px; background: var(--copper);
  }
  .address {
    margin-top: 48px;
    font-size: 11.5px; color: var(--text-light);
  }
  .contact {
    display: inline-flex; gap: 16px; align-items: center;
    margin-top: 8px; padding: 6px 10px;
    border-top: 1px solid var(--copper-soft);
    border-bottom: 1px solid var(--copper-soft);
    font-size: 15px; color: var(--text-light);
  }
  .contact span { display: inline-flex; align-items: center; gap: 6px; }
  .contact svg { width: 13px; height: 13px; }
</style>
</head>
<body>
  <main class="poster">
    <div class="territory-map" role="img" aria-label="Silver silhouette map of the Principality of Monaco"></div>
    <h1 class="headline">un<br>nouveau<br>regard<br>sur<br>l'immobilier</h1>
    <div class="coast-photo" role="img" aria-label="Panoramic photograph of Monaco's coastline, harbour and rock above the blue sea"></div>
    <section class="brand">
      <div class="brand-name"><span class="brand-mark"></span>BRUNOR AGENCY</div>
      <p class="address">14 rue des Orvilles, Passage Marcellin, 98 000 Monaco</p>
      <div class="contact">
        <span>
          <svg viewBox="0 0 16 16"><circle cx="8" cy="8" r="8" fill="#dc9a80"/><path d="M5 4.5l1.6-.4 1 2-1 .8a5 5 0 002.5 2.5l.8-1 2 1-.4 1.6C8 11.5 4.5 8 5 4.5z" fill="#1c2a45"/></svg>
          +377.93.48.25.71
        </span>
        <span>
          <svg viewBox="0 0 16 16"><circle cx="8" cy="8" r="7" fill="none" stroke="#dc9a80" stroke-width="1.5"/><ellipse cx="8" cy="8" rx="3" ry="7" fill="none" stroke="#dc9a80" stroke-width="1.2"/><line x1="1" y1="8" x2="15" y2="8" stroke="#dc9a80" stroke-width="1.2"/></svg>
          www.brunor-agency.com.
        </span>
      </div>
    </section>
  </main>
</body>
</html>
```